Lottie's Clam Shack Website

We are looking to create an official website for our seafood restaurant with the following specifications:
Design style: modern, street, industrial and neon aesthetic; primary color palette: black, white and red.
Prominent placement for online ordering on the homepage.
Feature our current single location, plus a dedicated section/page for our upcoming second restaurant opening.
The site must be fully ADA compliant.
Full social media integration with linked profiles.
Include a floating contact/comment widget for customer inquiries and messages.
Mobile-first responsive design, optimized primarily for mobile users.
Preferred platform: Squarespace. Alternative option: Wix, for simple future self-maintenance and content updates.
The design should have unique personality and creative styling. We prefer a custom, distinctive look rather than a generic, rigid and standard template layout.

our ins:@lottiesclamshack

"snagashrimpwx.com" this is another restraunt like us, and we like their web, but please dont make us the same like theirs.

```html
<!DOCTYPE html>
<html lang="en">
<head>
<meta charset="utf-8">
<title>Lottie's Clam Shack</title>
<link href="https://fonts.googleapis.com/css2?family=Inter:wght@400;500;600;700;800;900&display=swap" rel="stylesheet">
<style>
:root{
  --stage:#a3a3a3;
  --black:#050506;
  --ink:#0b0b0d;
  --panel:#111113;
  --line:#222226;
  --white:#ffffff;
  --muted:#c9c9cc;
  --red:#e02a2a;
  --red-soft:#ff5a55;
  --red-deep:#b81c1f;
}
*{box-sizing:border-box;margin:0;padding:0}
html,body{width:1200px;height:2557px;overflow:hidden}
body{background:var(--stage);font-family:"Inter",sans-serif;color:var(--white)}
.page{position:absolute;left:63px;top:63px;width:1083px;height:2450px;background:var(--black);overflow:hidden}

/* nav */
.nav{position:absolute;left:0;top:0;width:100%;height:54px;background:#050505;border-bottom:1px solid #1c1c1c;z-index:3}
.brand{position:absolute;left:123px;top:16px;display:flex;align-items:center;gap:8px;font-weight:800;font-size:17px;letter-spacing:-.3px;color:var(--white)}
.brand-dot{width:14px;height:14px;border-radius:50%;background:var(--red)}
.nav-links{position:absolute;left:438px;top:20px;display:flex;gap:20px;font-size:10px;font-weight:500}
.order-btn{position:absolute;left:868px;top:10px;width:91px;height:33px;border-radius:17px;background:var(--red);font-size:11px;font-weight:700;display:flex;align-items:center;justify-content:center}

/* hero */
.hero{position:absolute;top:54px;left:0;width:100%;height:734px;
  background:
   radial-gradient(ellipse 520px 420px at 850px 60px,rgba(170,28,32,.55),transparent 70%),
   radial-gradient(ellipse 500px 360px at 1000px 700px,rgba(110,10,14,.6),transparent 70%),
   linear-gradient(#070707,#0b0808);
  overflow:hidden;border-bottom:1px solid #1a1a1a}
.hero-grid{position:absolute;inset:0;background-image:linear-gradient(rgba(255,255,255,.025) 1px,transparent 1px),linear-gradient(90deg,rgba(255,255,255,.025) 1px,transparent 1px);background-size:34px 34px}
.ghost{position:absolute;left:570px;top:560px;font-size:210px;font-weight:900;color:rgba(255,255,255,.035);transform:rotate(-22deg);transform-origin:left top;letter-spacing:-6px}
.badge{position:absolute;left:123px;top:183px;height:26px;padding:0 12px;border:1px solid rgba(224,42,42,.6);border-radius:13px;background:rgba(224,42,42,.12);display:flex;align-items:center;gap:6px;font-size:8.5px;font-weight:800;letter-spacing:1px;color:#ffd7d4}
.badge i{width:6px;height:8px;background:#ff8a2a;border-radius:50% 50% 50% 50%/60% 60% 40% 40%}
.headline{position:absolute;left:123px;top:236px;font-size:57px;line-height:55px;font-weight:800;letter-spacing:-3.8px}
.headline .hot{color:var(--red-soft)}
.lede{position:absolute;left:123px;top:418px;width:410px;font-size:13.5px;line-height:23px;color:#e8e8e8}
.cta{position:absolute;top:505px;height:42px;border-radius:8px;display:flex;align-items:center;justify-content:center;font-size:13px;font-weight:700}
.cta-order{left:123px;width:138px;background:var(--red);box-shadow:0 8px 24px rgba(224,42,42,.35)}
.cta-call{left:273px;width:160px;border:1px solid #55555a;background:rgba(0,0,0,.3)}
.flavor-card{position:absolute;left:562px;top:148px;width:397px;height:425px;border:1px solid rgba(255,255,255,.12);border-radius:22px;background:rgba(255,255,255,.035)}
.flavor-inner{position:absolute;left:14px;top:14px;width:368px;height:396px;border-radius:18px;background:radial-gradient(circle at 50% 40%,rgba(224,42,42,.55),transparent 55%),#0a0a0b;overflow:hidden}
.flavor-tags{position:absolute;top:20px;left:20px;right:20px;display:flex;justify-content:space-between;font-size:8.5px;font-weight:700;letter-spacing:3px;color:#cfcfcf}
.ring{position:absolute;left:82px;top:95px;width:204px;height:204px;border-radius:50%;border:12px solid #c8282b;background:radial-gradient(circle at 50% 30%,#b01e22,#2a0506 70%,#120203);box-shadow:0 0 40px rgba(224,42,42,.55)}
.ring-mark{position:absolute;left:75px;top:30px;width:30px;height:30px;border-radius:50%;background:#f06a2a}
.ring-title{position:absolute;top:104px;width:100%;text-align:center;font-size:20px;font-weight:800;letter-spacing:-1px}
.ring-sub{position:absolute;top:153px;width:100%;text-align:center;font-size:10.5px;color:#eee}
.pills{position:absolute;left:16px;right:16px;top:347px;display:flex;gap:9px}
.pills span{flex:1;height:31px;border:1px solid #333;border-radius:15px;background:#050505;font-size:10px;font-weight:700;display:flex;align-items:center;justify-content:center}

/* menu */
.menu{position:absolute;top:788px;left:0;width:100%;height:409px;background:var(--ink);border-bottom:1px solid #1a1a1a}
.eyebrow{position:absolute;left:123px;top:73px;font-size:11px;font-weight:800;letter-spacing:3.5px;color:var(--red-soft)}
.section-title{position:absolute;left:123px;top:94px;font-size:38px;font-weight:800;letter-spacing:-1.2px}
.more{position:absolute;left:863px;top:131px;font-size:11px;font-weight:700;color:#ff8f8a}
.dishes{position:absolute;left:123px;top:171px;width:836px;display:flex;gap:12px}
.dish{width:200px;height:176px;border:1px solid #232326;border-radius:16px;background:#030303;padding:18px 18px}
.price{font-size:22px;font-weight:800;color:var(--red-soft);letter-spacing:-.5px}
.dish h3{font-size:14.5px;font-weight:700;margin-top:15px;letter-spacing:-.3px}
.dish p{font-size:11px;line-height:19px;color:#cfcfd2;margin-top:8px}

/* flavors */
.flavors{position:absolute;top:1197px;left:0;width:100%;height:377px;background:#060607;border-bottom:1px solid #181818}
.heat-card{position:absolute;left:123px;top:62px;width:274px;height:253px;border-radius:18px;background:var(--red);box-shadow:0 0 40px rgba(224,42,42,.3);padding:0 24px}
.heat-card svg{position:absolute;left:24px;top:52px}
.heat-card h2{position:absolute;left:24px;top:100px;font-size:38px;line-height:40px;font-weight:800;letter-spacing:-1.3px}
.options{position:absolute;left:412px;top:62px;width:547px;height:253px;border:1px solid #26262a;border-radius:18px;background:var(--panel)}
.opt{position:absolute;top:36px;width:240px}
.opt h4{font-size:12.5px;font-weight:700;color:var(--red-soft)}
.opt p{font-size:11px;line-height:19px;color:#cfcfd2;margin-top:10px}

/* locations */
.locations{position:absolute;top:1574px;left:0;width:100%;height:470px;background:var(--black);border-bottom:1px solid #161616}
.loc{position:absolute;top:62px;width:410px;height:347px;border-radius:18px;padding:0 24px}
.loc-now{left:123px;border:1px solid #232326;background:#0a0a0b}
.loc-next{left:549px;border:1px solid #4a1416;background:radial-gradient(circle at 0 0,#2a0809,#0d0505 70%)}
.loc svg.icon{position:absolute;left:24px;top:55px}
.loc h2{position:absolute;left:24px;top:112px;font-size:37px;line-height:40px;font-weight:800;letter-spacing:-1.2px}
.addr{position:absolute;left:24px;top:170px;font-size:14px;line-height:25px;font-weight:700}
.hours{position:absolute;left:24px;top:231px;font-size:11px;line-height:19px;color:#cfcfd2}
.loc-next p{position:absolute;left:24px;top:204px;width:362px;font-size:11px;line-height:19px;color:#d4d4d6}
.updates{position:absolute;left:24px;top:286px;width:153px;height:36px;border-radius:9px;background:var(--white);color:#0a0a0a;font-size:11px;font-weight:700;display:flex;align-items:center;justify-content:center}

/* features */
.features{position:absolute;top:2044px;left:0;width:100%;height:275px;background:var(--black)}
.feat-row{position:absolute;left:123px;top:63px;display:flex;gap:13px}
.feat{width:270px;height:150px;border:1px solid #232326;border-radius:16px;background:#080809;padding:0 18px}
.feat h3{margin-top:32px;font-size:14.5px;font-weight:700;display:flex;align-items:center;gap:5px;letter-spacing:-.3px}
.feat h3 i{width:14px;height:14px;border-radius:3px;background:#3b82f6;display:inline-block}
.feat p{margin-top:11px;font-size:11px;line-height:19px;color:#cfcfd2}

/* footer */
.footer{position:absolute;top:2319px;left:0;width:100%;height:131px;background:var(--red-deep)}
.footer h2{position:absolute;left:123px;top:34px;font-size:24px;font-weight:800;letter-spacing:-.8px}
.footer p{position:absolute;left:123px;top:75px;font-size:11px}
.socials{position:absolute;right:124px;top:49px;display:flex;gap:8px}
.socials span{height:33px;padding:0 13px;border-radius:17px;background:#0a0a0a;font-size:11px;font-weight:700;display:flex;align-items:center}
</style>
</head>
<body>
<div class="page">

  <header class="nav">
    <div class="brand"><span class="brand-dot"></span>Lottie's Clam Shack</div>
    <nav class="nav-links"><span>Menu</span><span>Location</span><span>2nd Opening</span><span>Contact</span></nav>
    <div class="order-btn">Order Now</div>
  </header>

  <section class="hero">
    <div class="hero-grid"></div>
    <div class="ghost">CRAB</div>
    <div class="badge"><i></i>CEDAR BAY SEAFOOD BOIL</div>
    <h1 class="headline">Crack shells.<br><span class="hot">Bring heat.</span> Eat<br>loud.</h1>
    <p class="lede">A modern street-style seafood house serving bold Cajun boils, snow crab plates, fried baskets, wings, sides and Lotties Bomb flavor.</p>
    <div class="cta cta-order">Online Ordering</div>
    <div class="cta cta-call">Call 555-014-2290</div>

    <div class="flavor-card">
      <div class="flavor-inner">
        <div class="flavor-tags"><span>CAJUN</span><span>GARLIC</span><span>BOMB</span></div>
        <div class="ring">
          <div class="ring-mark" role="img" aria-label="Small crab illustration"></div>
          <div class="ring-title">LOTTIES BOMB</div>
          <div class="ring-sub">Most Popular Flavor</div>
        </div>
        <div class="pills"><span>Snow Crab</span><span>Shrimp</span><span>Crawfish</span></div>
      </div>
    </div>
  </section>

  <section class="menu">
    <div class="eyebrow">MENU HIGHLIGHTS</div>
    <h2 class="section-title">Seafood built for sharing.</h2>
    <div class="more">View full menu →</div>
    <div class="dishes">
      <article class="dish"><div class="price">$40</div><h3>Seafood Plate 2 LB</h3><p>Choice of shrimp, clams, mussels or crawfish with corn, sausage and potato.</p></article>
      <article class="dish"><div class="price">$60</div><h3>Snow Crab Plate</h3><p>1LB snow crab + 1LB choice of shrimp, clams, mussels or crawfish.</p></article>
      <article class="dish"><div class="price">$140</div><h3>Seafood Deluxe</h3><p>6 clusters snow crab, 1LB seafood choice, sausage, corn, potatoes and eggs.</p></article>
      <article class="dish"><div class="price">$15</div><h3>Fried Shrimp Basket</h3><p>Crispy fried shrimp served with a side.</p></article>
    </div>
  </section>

  <section class="flavors">
    <div class="heat-card">
      <svg width="24" height="20" viewBox="0 0 24 20" aria-hidden="true"><circle cx="12" cy="10" r="8" fill="#fff"/><circle cx="12" cy="10" r="5" fill="#ddd"/><rect x="0" y="2" width="2" height="16" fill="#eee"/><rect x="22" y="2" width="2" height="16" fill="#eee"/></svg>
      <h2>Pick your flavor. Pick your heat.</h2>
    </div>
    <div class="options">
      <div class="opt" style="left:24px"><h4>Flavors</h4><p>Cajun Classic · Garlic Butter · Lemon Pepper · Lotties Bomb</p></div>
      <div class="opt" style="left:284px"><h4>Spice Levels</h4><p>Non-Spicy · Mild · Medium · Extreme Hot</p></div>
    </div>
  </section>

  <section class="locations">
    <article class="loc loc-now">
      <svg class="icon" width="12" height="22" viewBox="0 0 12 22" aria-hidden="true"><line x1="6" y1="8" x2="6" y2="22" stroke="#999" stroke-width="2"/><circle cx="6" cy="6" r="5" fill="#e02a2a"/></svg>
      <h2>Current Location</h2>
      <div class="addr">4820 Harbor Ln.<br>Cedar Bay, CA 90000</div>
      <div class="hours">Monday–Friday 3pm–9pm · Closed Tuesday<br>Saturday–Sunday 12noon–10pm</div>
    </article>
    <article class="loc loc-next">
      <svg class="icon" width="24" height="24" viewBox="0 0 24 24" aria-hidden="true"><polygon points="12,1 15,9 23,9 17,14 19,22 12,17 5,22 7,14 1,9 9,9" fill="#f2b02e"/></svg>
      <h2>Second Restaurant Opening Soon</h2>
      <p>A dedicated announcement page for the upcoming second location with opening date, address, grand opening offers, social updates, and email/SMS signup.</p>
      <div class="updates">Get Opening Updates</div>
    </article>
  </section>

  <section class="features">
    <div class="feat-row">
      <article class="feat"><h3><i></i>ADA First</h3><p>High contrast, keyboard navigation, visible focus states, semantic labels and alt-ready image areas.</p></article>
      <article class="feat"><h3><i style="background:#8a8a8a"></i>Social Connected</h3><p>Photo feed area, social profile links, review/order links, and share-ready content sections.</p></article>
      <article class="feat"><h3><i style="background:#e6e6e6;border-radius:50%"></i>Floating Widget</h3><p>Customer contact/comment bubble fixed on mobile and desktop for quick messages.</p></article>
    </div>
  </section>

  <footer class="footer">
    <h2>LOTTIE'S CLAM SHACK</h2>
    <p>Street-style seafood boil with a neon industrial attitude.</p>
    <div class="socials"><span>@lottiesclamshack</span><span>Call</span><span>Website</span></div>
  </footer>

</div>
</body>
</html>
```